Menu: A4 (double sided) Lunch/Dinner Menu (one side) + Pizza Menu (other side)

Hello.
We would like to create a new style of menus.
Must be easy to read - a summer feel, crisp, clean, beachy, possible retro feel, colours probably based on our website colours (see address below).
Simple and casual is best as we are a casual beachside Cafe.
This menu will be double sided therefore this job is 2 pages.
If you win this job we will have 2 or 3 more menus for you to create soon after (Drinks, Breakfast, possibly a small Kids menu).
The paper for these menus we expect will be a nice white paper which will then be matte laminated.
Colours possible are the green colour #3a6066, the terracotta on our website logo border and website buttons, maybe a little yellow but must be easy to read on white paper.
Black for text might be okay if this is your best design option.
Please view our website and take a feel for the business, location, the existing website branding and website colours we are trying to achieve, www.tidelinekitchen.com.au
We prefer to avoid overwhelming the guest with too many colours on the menus (hence the white paper) as the building is so colourful (El Prado, Argentina, inspired) and the guest experience can be complimented via crisp easy to read menus.
IMPORTANT:
The menus provided please must be fully and easily editable by us in the future.
If you win the job, you must please provide clear instructions on how our staff can edit the menus in the future if project is delivered in Adobe format. Word is also an option for us if you like.
As such, we have attached some documents: the 2x Word documents for the text, 2x .pdf so you can see the fonts and style we were using previously (was printing on recycled brown paper then matte laminated).
If you wished to use the SeaLife Font (this is the existing Font for headings) please let us know as we purchased that font and can provide it.
We have also attached a menu from Marlowe Tavern which we feel has a nice retro feel.
Please include our Instagram in 1 place on the menu @tidelinekitchen
Finally, please note,
we never wish to waste anyone's time so we will narrow down the submissions quickly based on first drafts (please know this is because we appreciate your effort and know your time is valuable) and we will then work with the top designer to finalise in a professional fashion.
Thank you.

```html
<!DOCTYPE html>
<html lang="en">
<head>
<meta charset="utf-8">
<title>Tideline Kitchen Menus</title>
<link rel="stylesheet" href="https://fonts.googleapis.com/css2?family=Montserrat:wght@400;500;600;700;800;900&family=Oswald:wght@500;600&display=swap">
<style>
:root{
  --navy:#1f4f8f;
  --teal:#3a6066;
  --terracotta:#c9532b;
  --yellow:#ffea00;
  --ink:#222222;
  --paper:#f1f0ec;
  --paper-edge:#e4e2dc;
  --backdrop:#ffffff;
}
*{box-sizing:border-box;margin:0;padding:0}
html,body{width:1200px;height:3481px;overflow:hidden}
body{background:var(--backdrop);font-family:'Montserrat',sans-serif;color:var(--ink);position:relative}
.menu-page{position:absolute;left:60px;width:1080px;height:1524px;background:var(--paper);box-shadow:0 10px 28px rgba(0,0,0,.28);overflow:hidden}
.menu-page--pizza{top:144px}
.menu-page--lunch{top:1812px}
.page-texture{position:absolute;inset:0;background:radial-gradient(circle at 50% 45%,#f6f5f1 0%,var(--paper) 60%,var(--paper-edge) 100%)}
.brand{position:absolute;left:46px;top:60px;display:flex;align-items:center;gap:16px}
.brand-square{width:44px;height:44px;background:var(--yellow)}
.brand-name{font-family:'Montserrat',sans-serif;font-weight:900;font-size:38px;line-height:1;color:var(--navy);letter-spacing:.5px}
.title{position:absolute;text-align:center;font-weight:900;line-height:.86}
.title-main{font-size:120px;color:var(--ink);letter-spacing:-2px}
.title-sub{font-size:112px;color:var(--teal);letter-spacing:-1px}
.title-sub-small{font-family:'Montserrat',sans-serif;font-weight:700;font-size:42px;color:var(--navy);display:flex;align-items:center;gap:12px;justify-content:center;margin-top:18px}
.swoosh{position:absolute}
.key-band{position:absolute;left:46px;width:978px;height:30px;background:var(--navy);color:#fff;font-weight:700;font-size:19px;display:flex;align-items:center;gap:64px;padding-left:110px;letter-spacing:.3px}
.section-banner{position:absolute;height:46px;background:var(--yellow);font-family:'Oswald',sans-serif;font-weight:600;font-size:34px;color:var(--ink);display:flex;align-items:center;justify-content:center;clip-path:polygon(4% 0,96% 0,100% 100%,0 100%);letter-spacing:.5px}
.art{position:absolute;border-radius:50%}
.pizza-item{position:absolute}
.pizza-item h4{font-weight:700;font-size:16px;color:var(--terracotta);letter-spacing:.2px}
.pizza-item p{font-size:15.5px;line-height:1.25;color:var(--ink);max-width:370px}
.price{position:absolute;right:0;top:6px;width:40px;height:28px;background:var(--teal);color:#fff;font-weight:600;font-size:17px;display:flex;align-items:center;justify-content:center;clip-path:polygon(14% 0,100% 0,100% 100%,0 100%)}
.entree-item{position:absolute;font-size:16px;line-height:1.3}
.entree-line{display:flex;align-items:flex-end;gap:6px;padding-right:52px}
.entree-line .leader{flex:1;border-bottom:2px dotted #777;margin-bottom:5px;min-width:20px}
.entree-item .price{top:0}
.veg{color:var(--terracotta);font-weight:600}
.mains-box{position:absolute;left:50px;top:630px;width:485px;height:751px;border:4px solid var(--yellow);background:#fff}
.main-item{position:absolute;left:76px;width:422px;font-size:15.5px;line-height:1.3}
.main-item .text{width:350px;border-bottom:2px dotted #888;padding-bottom:2px}
.main-item .price{top:4px}
.platter-banner{position:absolute;left:583px;top:577px;width:433px;height:75px;background:var(--teal);color:#fff;font-family:'Oswald',sans-serif;font-weight:500;font-size:34px;display:flex;align-items:center;justify-content:center}
.side-item{position:absolute;left:586px;width:422px;font-size:15.5px;line-height:1.3}
.side-item h4{font-weight:700;font-size:16px;color:var(--terracotta)}
.side-item .text{width:360px;border-bottom:2px dotted #888;padding-bottom:2px}
.side-item .price{top:2px}
.small-note{font-size:13.5px;line-height:1.3}
.footer-address{position:absolute;left:66px;top:1402px;display:flex;gap:22px;align-items:center;font-size:21px;line-height:1.25}
.badges{position:absolute;top:1406px;left:490px;display:flex;gap:22px;align-items:center}
.badge{width:72px;height:72px;border-radius:50%;background:var(--yellow);border:3px solid #e2a400;color:var(--terracotta);font-size:9.5px;font-weight:700;text-align:center;display:flex;align-items:center;justify-content:center;line-height:1.15;padding:6px}
.badge--book{width:112px;border-radius:14px;font-size:12px}
</style>
</head>
<body>

<!-- Pizza side -->
<section class="menu-page menu-page--pizza" aria-label="Pizza menu">
  <div class="page-texture" role="img" aria-label="Faint hand-drawn food doodle pattern"></div>

  <div class="brand"><span class="brand-square"></span><span class="brand-name">TIDELINE<br>KITCHEN</span></div>

  <svg class="swoosh" style="left:455px;top:110px" width="60" height="90" viewBox="0 0 60 90"><path d="M4 10 Q30 14 52 26 Q30 24 4 10Z M2 40 Q30 40 56 46 Q30 50 2 40Z M8 80 Q26 66 50 58 Q30 74 8 80Z" fill="var(--navy)"/></svg>
  <svg class="swoosh" style="left:945px;top:110px" width="60" height="90" viewBox="0 0 60 90"><path d="M56 10 Q30 14 8 26 Q30 24 56 10Z M58 40 Q30 40 4 46 Q30 50 58 40Z M52 80 Q34 66 10 58 Q30 74 52 80Z" fill="var(--navy)"/></svg>
  <div class="title" style="left:515px;top:50px;width:430px"><div class="title-main">MENU</div><div class="title-sub">PIZZA</div></div>

  <div class="key-band" style="top:248px"><span>V&nbsp; VEGETARIAN</span><span>GFO&nbsp; GLUTEN FRIENDLY OPTIONAL, PLEASE ASK</span></div>

  <div class="art" role="img" aria-label="Drawing of a pizza slice" style="left:262px;top:284px;width:136px;height:100px;background:#f4e27a;border-radius:40% 60% 30% 70%"></div>
  <div class="section-banner" style="left:408px;top:295px;width:272px">STANDARD</div>
  <div class="art" role="img" aria-label="Drawing of a burger" style="left:680px;top:290px;width:134px;height:90px;background:#f2dc5e"></div>

  <div class="pizza-item" style="left:80px;top:375px;width:405px"><h4>HAWAIIAN</h4><p>ham, pineapple</p><span class="price">22</span></div>
  <div class="pizza-item" style="left:80px;top:433px;width:405px"><h4>MARGHERITA</h4><p>v&nbsp; marinated &amp; diced tomatoes,<br>fresh basil</p><span class="price">22</span></div>
  <div class="pizza-item" style="left:80px;top:511px;width:405px"><h4>BBQ CHICKEN</h4><p>chicken, salami, tomato, spanish<br>onion, bbq sauce</p><span class="price">26</span></div>
  <div class="pizza-item" style="left:80px;top:589px;width:405px"><h4>CHORIZO</h4><p>chorizo, salami, tomato,<br>mushrooms, spanish onion</p><span class="price">26</span></div>
  <div class="pizza-item" style="left:80px;top:668px;width:405px"><h4>TIDELINE SPECIAL</h4><p>ham, salami, prawns, kalamata olives,<br>roasted capsicum, mushrooms, spanish onion</p><span class="price">26</span></div>
  <div class="pizza-item" style="left:80px;top:746px;width:405px"><h4>MEAT LOVERS</h4><p>chicken, bacon, salami, ham,<br>bbq sauce</p><span class="price">26</span></div>

  <div class="pizza-item" style="left:568px;top:375px;width:422px"><h4>HAWAIIAN</h4><p>ham, pineapple</p><span class="price">22</span></div>
  <div class="pizza-item" style="left:568px;top:433px;width:422px"><h4>MARGHERITA</h4><p>v&nbsp; marinated &amp; diced tomatoes,<br>fresh basil</p><span class="price">22</span></div>
  <div class="pizza-item" style="left:568px;top:511px;width:422px"><h4>BBQ CHICKEN</h4><p>chicken, salami, tomato, spanish<br>onion, bbq sauce</p><span class="price">26</span></div>
  <div class="pizza-item" style="left:568px;top:589px;width:422px"><h4>CHORIZO</h4><p>chorizo, salami, tomato,<br>mushrooms, spanish onion</p><span class="price">26</span></div>
  <div class="pizza-item" style="left:568px;top:668px;width:422px"><h4>TIDELINE SPECIAL</h4><p>ham, salami, prawns, kalamata olives,<br>roasted capsicum, mushrooms, spanish onion</p><span class="price">26</span></div>
  <div class="pizza-item" style="left:568px;top:746px;width:422px"><h4>MEAT LOVERS</h4><p>chicken, bacon, salami, ham,<br>bbq sauce</p><span class="price">26</span></div>

  <div class="art" role="img" aria-label="Drawing of a hot dog" style="left:249px;top:808px;width:142px;height:90px;background:#f3e06a;border-radius:45%"></div>
  <div class="section-banner" style="left:408px;top:842px;width:272px">GOURMET</div>
  <div class="art" role="img" aria-label="Drawing of a whole round pizza" style="left:693px;top:813px;width:177px;height:115px;background:#f6e040"></div>

  <div class="pizza-item" style="left:80px;top:922px;width:405px"><h4>HAWAIIAN</h4><p>ham, pineapple</p><span class="price">22</span></div>
  <div class="pizza-item" style="left:80px;top:980px;width:405px"><h4>MARGHERITA</h4><p>v&nbsp; marinated &amp; diced tomatoes,<br>fresh basil</p><span class="price">22</span></div>
  <div class="pizza-item" style="left:80px;top:1059px;width:405px"><h4>BBQ CHICKEN</h4><p>chicken, salami, tomato, spanish<br>onion, bbq sauce</p><span class="price">26</span></div>
  <div class="pizza-item" style="left:80px;top:1137px;width:405px"><h4>CHORIZO</h4><p>chorizo, salami, tomato,<br>mushrooms, spanish onion</p><span class="price">26</span></div>
  <div class="pizza-item" style="left:80px;top:1215px;width:405px"><h4>TIDELINE SPECIAL</h4><p>ham, salami, prawns, kalamata olives,<br>roasted capsicum, mushrooms, spanish onion</p><span class="price">26</span></div>
  <div class="pizza-item" style="left:80px;top:1293px;width:405px"><h4>MEAT LOVERS</h4><p>chicken, bacon, salami, ham,<br>bbq sauce</p><span class="price">26</span></div>

  <div class="pizza-item" style="left:568px;top:922px;width:422px"><h4>HAWAIIAN</h4><p>ham, pineapple</p><span class="price">22</span></div>
  <div class="pizza-item" style="left:568px;top:980px;width:422px"><h4>MARGHERITA</h4><p>v&nbsp; marinated &amp; diced tomatoes,<br>fresh basil</p><span class="price">22</span></div>
  <div class="pizza-item" style="left:568px;top:1059px;width:422px"><h4>BBQ CHICKEN</h4><p>chicken, salami, tomato, spanish<br>onion, bbq sauce</p><span class="price">26</span></div>
  <div class="pizza-item" style="left:568px;top:1137px;width:422px"><h4>CHORIZO</h4><p>chorizo, salami, tomato,<br>mushrooms, spanish onion</p><span class="price">26</span></div>
  <div class="pizza-item" style="left:568px;top:1215px;width:422px"><h4>TIDELINE SPECIAL</h4><p>ham, salami, prawns, kalamata olives,<br>roasted capsicum, mushrooms, spanish onion</p><span class="price">26</span></div>
  <div class="pizza-item" style="left:568px;top:1293px;width:422px"><h4>MEAT LOVERS</h4><p>chicken, bacon, salami, ham,<br>bbq sauce</p><span class="price">26</span></div>

  <div class="footer-address">
    <svg width="26" height="34" viewBox="0 0 26 34"><path d="M13 2C7 2 3 6.5 3 12c0 7 10 18 10 18s10-11 10-18C23 6.5 19 2 13 2Z" fill="none" stroke="var(--ink)" stroke-width="3"/><circle cx="13" cy="12" r="4" fill="var(--ink)"/></svg>
    <div>88 Shoreline Parade<br>88 Shoreline Parade, Saltbay SA 5999</div>
  </div>
  <div class="badges">
    <div class="badge">Download Lunch+Dinner Menu</div>
    <div class="badge">Download Takeaway Flyer</div>
    <div class="badge">Buy a Gift Card</div>
    <div class="badge">Download Breakfast Menu</div>
    <div class="badge badge--book">Click Here to Book Now</div>
  </div>
</section>

<!-- Lunch + dinner side -->
<section class="menu-page menu-page--lunch" aria-label="Lunch and dinner menu">
  <div class="page-texture" role="img" aria-label="Faint hand-drawn food doodle pattern"></div>

  <div class="brand"><span class="brand-square"></span><span class="brand-name">TIDELINE<br>KITCHEN</span></div>

  <div class="title" style="left:470px;top:50px;width:480px">
    <div class="title-main">MENU</div>
    <div class="title-sub-small">
      <svg width="36" height="40" viewBox="0 0 36 40"><path d="M4 4 Q20 6 32 14 Q18 12 4 4Z M2 20 Q18 19 34 22 Q18 25 2 20Z M6 36 Q18 28 30 26 Q20 34 6 36Z" fill="var(--navy)"/></svg>
      LUNCH + DINNER
      <svg width="36" height="40" viewBox="0 0 36 40"><path d="M32 4 Q16 6 4 14 Q18 12 32 4Z M34 20 Q18 19 2 22 Q18 25 34 20Z M30 36 Q18 28 6 26 Q16 34 30 36Z" fill="var(--navy)"/></svg>
    </div>
  </div>

  <div class="key-band" style="top:254px"><span>V&nbsp; VEGETARIAN</span><span>GFO&nbsp; GLUTEN FRIENDLY OPTIONAL, PLEASE ASK</span></div>

  <div class="section-banner" style="left:408px;top:297px;width:222px">ENTREE</div>
  <div class="art" role="img" aria-label="Drawing of a plated dish" style="left:657px;top:284px;width:68px;height:70px;background:#d8d6d0"></div>

  <div class="entree-item" style="left:50px;top:372px;width:373px"><div class="entree-line"><span>Garlic Bread (2)&nbsp; <span class="veg">v</span></span><span class="leader"></span></div><span class="price">8</span></div>
  <div class="entree-item" style="left:50px;top:414px;width:373px"><div class="entree-line"><span>Salt &amp; Pepper Squid&nbsp; w/ thai</span><span class="leader"></span></div>dipping sauce<span class="price">18</span></div>
  <div class="entree-item" style="left:50px;top:478px;width:373px"><div class="entree-line"><span>Duo of Dip&nbsp; <span class="veg">v</span>&nbsp; w/ pita</span><span class="leader"></span></div><span class="price">14</span></div>
  <div class="entree-item" style="left:50px;top:522px;width:373px"><div class="entree-line"><span>Bowl of Chips&nbsp; <span class="veg">v</span>&nbsp; w/ tomato sauce</span><span class="leader"></span></div><span class="price">11</span></div>

  <div class="entree-item" style="left:462px;top:372px;width:529px"><div class="entree-line"><span>Seasoned Wedges&nbsp; <span class="veg">v</span>&nbsp; w/ sour cream &amp; sweet chilli</span><span class="leader"></span></div><span class="price">15</span></div>
  <div class="entree-item" style="left:462px;top:416px;width:529px"><div class="entree-line"><span>Onion Rings (12)&nbsp; <span class="veg">v</span>&nbsp; beer battered w/ tangy mayo</span><span class="leader"></span></div><span class="price">13</span></div>
  <div class="entree-item" style="left:462px;top:460px;width:529px"><div class="entree-line"><span>Vietnamese Spring Rolls (3)&nbsp; chicken, home-made</span><span class="leader"></span></div><span class="price">11</span></div>
  <div class="entree-item" style="left:462px;top:504px;width:529px"><div class="entree-line"><span>Bruschetta (1)&nbsp; <span class="veg">v</span>&nbsp; w/ olive oil, tomato &amp; red onion</span><span class="leader"></span></div>salsa, balsamic glaze, feta<span class="price">10</span></div>

  <div class="mains-box"></div>
  <div class="section-banner" style="left:156px;top:607px;width:204px">MAINS</div>
  <div class="art" role="img" aria-label="Drawing of a plated meal" style="left:360px;top:600px;width:128px;height:57px;background:#d8d6d0"></div>

  <div class="main-item" style="top:710px"><div class="text">THE FISH &amp; CHIPS&nbsp; house-crumbed butterfish w/ chips, tartare &amp; side salad</div><span class="price">25</span></div>
  <div class="main-item" style="top:799px"><div class="text">Smokey beef &amp; bacon cheese burger w/ chips, onion rings, gerkins &amp; tangy mayo<br>+ jalapenos&nbsp; 2&nbsp;&nbsp; + pineapple&nbsp; 2</div><span class="price">23</span></div>
  <div class="main-item" style="top:907px"><div class="text">SALT &amp; PEPPER SQUID&nbsp; golden tangles w/ chips, thai dipping sauce &amp; side salad</div><span class="price">31</span></div>
  <div class="main-item" style="top:994px"><div class="text">SEAFOOD BASKET&nbsp; crumbed butterfish, grilled prawns, salt &amp; pepper squid, chips, tartare &amp; side salad</div><span class="price">31</span></div>
  <div class="main-item" style="top:1100px"><div class="text">ATLANTIC SALMON&nbsp; served w/ mash, teriyaki sauce &amp; winter vegetables<br>(contains breadcrumbs)</div><span class="price">31</span></div>
  <div class="main-item" style="top:1210px"><div class="text">CHICKEN PARMIGIANA&nbsp; house-crumbed breast schnitzel, napoli sauce, mozzarella, chips &amp; side salad<br>+ bacon and pineapple&nbsp; 4<br>+ jalapenos and pineapple</div><span class="price">27</span></div>

  <div class="platter-banner">TIDELINE PLATTER FOR 2</div>
  <div class="side-item small-note" style="top:664px;width:430px">beer battered flathead, salt &amp; pepper squid, prawn skewers, grilled chicken, lamb &amp; chorizo,served with antipasto, dipping sauces, pita &amp; garlic bread&nbsp; 90&nbsp;&nbsp; (+45 pp)</div>
  <div class="side-item" style="top:758px"><div class="text">New York sirloin&nbsp; gfo&nbsp; 400g MSA w/ mash &amp; winter vegetables choose: mushroom gravy or classic gravy or surf 'n' turf&nbsp; gfo&nbsp; +6</div><span class="price">38</span></div>
  <div class="side-item" style="top:864px"><div class="text">Please allow 35+ minutes for "well-done"</div><span class="price">27</span></div>
  <div class="side-item" style="top:912px"><h4>CHICKEN CAESAR</h4><div class="text">w/ bacon, anchovies, egg, caesar dressing, parmesan, spanish onion, garlic bread</div><span class="price">30</span></div>
  <div class="side-item" style="top:1024px"><h4>LAMB SALAD</h4><div class="text">gfo&nbsp; skewers w/ traditional greek salad, tzatziki &amp; garlic bread+ extra lamb</div><span class="price">26</span></div>
  <div class="side-item" style="top:1110px"><h4>tHAI CHICKEN CURRY</h4><div class="text">mild gfo&nbsp; traditional recipe, w/ jasmine rice &amp; papadums</div><span class="price">23</span></div>
  <div class="side-item" style="top:1198px"><h4>BEACH BURGEr</h4><div class="text">v&nbsp; house-made pea &amp; corn ricotta fritter, pineapple, w/ wedges, onion rings, sweet chilli</div><span class="price">24</span></div>
  <div class="side-item" style="top:1306px"><h4>VEGAN CURRY</h4><div class="text">mild&nbsp; gfo v&nbsp; chickpea &amp; pumpkin w/ fresh tomatoes &amp; basil, jasmine rice &amp; papadums</div><span class="price" style="top:-20px">24</span></div>

  <div class="footer-address" style="top:1420px">
    <svg width="26" height="34" viewBox="0 0 26 34"><path d="M13 2C7 2 3 6.5 3 12c0 7 10 18 10 18s10-11 10-18C23 6.5 19 2 13 2Z" fill="none" stroke="var(--ink)" stroke-width="3"/><circle cx="13" cy="12" r="4" fill="var(--ink)"/></svg>
    <div>88 Shoreline Parade<br>88 Shoreline Parade, Saltbay SA 5999</div>
  </div>
  <div class="badges" style="top:1424px">
    <div class="badge">Download Lunch+Dinner Menu</div>
    <div class="badge">Download Takeaway Flyer</div>
    <div class="badge">Buy a Gift Card</div>
    <div class="badge">Download Breakfast Menu</div>
    <div class="badge badge--book">Click Here to Book Now</div>
  </div>
</section>

</body>
</html>
```